Business Card Design Project

We are a commercial talent casting company, a very "now" company. We need a new business card that is both current, graphic and elegantly interesting. As we are a service business,
we need something that will attract the attention of new clients,
yet project a business that is 25 years old.

Industry/Entity Type

Business

Requirements
Must have
• 1. Logo - Nora Quillan Casting
2. Address - 47 Thornbury Street
New York, New York 10010
3. Phone - 212-738-4192
4. E-Mail - Casting@noraquillan.example

Nice to have
• Would like the card in black and white with the only accent
color being red.

```html
<!DOCTYPE html>
<html lang="en">
<head>
<meta charset="utf-8">
<title>Nora Quillan Casting — Business Card</title>
<link rel="stylesheet" href="https://fonts.googleapis.com/css2?family=Open+Sans:wght@400;500&display=swap">
<style>
  :root {
    --card-black: #0a0b0a;
    --accent-red: #ff0000;
    --text-white: #ffffff;
    --rule-grey: #8a8a8a;
  }
  html, body {
    margin: 0;
    padding: 0;
    width: 1200px;
    height: 686px;
    overflow: hidden;
    background: var(--card-black);
  }
  .business-card {
    display: block;
    width: 1200px;
    height: 686px;
  }
  .card-background { fill: var(--card-black); }
  .accent-band { fill: var(--accent-red); }
  .margin-rule { stroke: var(--rule-grey); stroke-width: 1.3; opacity: 0.8; }
  .company-name {
    font-family: "Open Sans", sans-serif;
    font-weight: 500;
    font-size: 58px;
    fill: var(--text-white);
  }
  .contact-line {
    font-family: "Open Sans", sans-serif;
    font-weight: 400;
    font-size: 41px;
    fill: var(--text-white);
  }
</style>
</head>
<body>
<svg class="business-card" viewBox="0 0 1200 686" xmlns="http://www.w3.org/2000/svg" role="img" aria-label="Nora Quillan Casting business card">
  <rect class="card-background" x="0" y="0" width="1200" height="686"/>
  <rect class="accent-band" x="0" y="128" width="1200" height="109"/>
  <line class="margin-rule" x1="129.5" y1="0" x2="129.5" y2="686"/>
  <line class="margin-rule" x1="171.5" y1="0" x2="171.5" y2="686"/>

  <text class="company-name" x="214" y="205">Nora Quillan Casting</text>

  <g class="contact-details">
    <text class="contact-line address-street" x="221" y="342">47 Thornbury Street</text>
    <text class="contact-line address-city" x="221" y="404">New York, New York 10010</text>
    <text class="contact-line phone" x="221" y="488">212-738-4192</text>
    <text class="contact-line email" x="221" y="573">Casting@noraquillan.example</text>
  </g>
</svg>
</body>
</html>
```